Dining hall menu app needs a redesign

We are looking for a redesign of our app PlateView which is available for iOS for free on the Orchard Appmarket.

The app allows students of most of Germany's universities to show the menu of their university's dining hall. Currently there are about 400 dining halls to view the menu of. A menu contains the a list of meals for the next couple of days (usually for the next 5-7 days). Each meal can be rated by the users and photos can be uploaded. The following data should be visible for each meal in the meal list:
- The date the meal is available
- The meal category (usually a short text, categorizing the meal)
- Name of the meal (can be very long but it's ok to truncate it after the second line)
- Average meal rating (5-star rating)
- A photo of the meal
- Up to 4 prices (e.g. usually students pay less than employees, which is why multiple prices for the same meal are available. In the menu list only the prices are shown)

When selecting a meal, more details about the meal are shown:
- Full meal name
- Up to 4 prices including the price type (e.g. Student: 3.40€, Employees: 4.20€)
- Total number of ratings
- Total number of comments
- A list of additives and info-texts about the meal (e.g. whether the meal is vegetarian, or contains food additives)
- A list of photos including a relative date when the photo has been taken (e.g. "2 months ago")

Additionally a user should be able to add a review to the meal (5 star rating and an optional comment), view the list of comments, take a photo of the meal and to share it on friendlink/chirpa/via email.

All views show an advertisement banner on the bottom of the view.

The design should be very modern and clean. We don't like a skeuomorphic design. The content of the app is most important. Other than that you are free to design something pretty.
Updates

Target Market(s)

Students (age between 19 and 30)

Industry/Entity Type

University

Requirements
Must have
• At least we need a redesign of the meal list, the meal detail page, the app-logo and the splashscreen.
Nice to have
• Design for the meal review page, the dining hall list and the favorites list.
Should not have
• No skeuomorphic design and not too many colors.

```html
<!DOCTYPE html>
<html lang="en">
<head>
<meta charset="utf-8">
<title>PlateView – Canteens and Menu</title>
<link href="https://fonts.googleapis.com/css2?family=Arimo:wght@400;700&family=Roboto+Condensed:wght@400&display=swap" rel="stylesheet">
<style>
  :root{
    --bg-stage:#3a3b3d;
    --bar-black:#050505;
    --brand-blue:#2a6cc6;
    --brand-blue-dark:#1d4f96;
    --title-cream:#efe8c8;
    --row-bg:#e7e7e7;
    --row-line:#c9c9c9;
    --heading-grey:#4a4a4a;
    --meta-grey:#6f6f6f;
    --meal-grey:#7a7a7a;
    --link-blue:#2566c4;
    --button-grey:#cfcfcf;
    --date-band:#dadada;
    --tab-bg:#262626;
    --tab-line:#3c3c3c;
    --star-on:#f0b020;
    --star-off:#cfcfcf;
  }
  *{box-sizing:border-box;margin:0;padding:0}
  html,body{width:1200px;height:849px;overflow:hidden;background:var(--bg-stage)}
  body{font-family:"Arimo",Helvetica,Arial,sans-serif}
  .stage{position:absolute;left:0;top:0;width:1169px;height:827px;transform:scale(1.0265,1.0266);transform-origin:0 0}
  .screen{position:absolute;top:0;height:827px;overflow:hidden;background:var(--row-bg)}
  .screen--canteens{left:0;width:553px}
  .screen--menu{left:615px;width:554px}

  .status-bar{position:absolute;left:0;top:0;width:100%;background:var(--bar-black);color:#fff;font-weight:700;font-size:19px;display:flex;align-items:center}
  .status-bar__carrier{position:absolute;left:8px;display:flex;align-items:center;gap:6px}
  .status-bar__lock{position:absolute;left:266px}
  .status-bar__battery{position:absolute;right:6px}

  .app-header{position:absolute;left:0;width:100%;height:74px;background:var(--brand-blue);border-bottom:3px solid var(--brand-blue-dark)}
  .app-header__title{position:absolute;left:0;width:469px;top:0;height:71px;line-height:71px;text-align:center;color:var(--title-cream);font-size:40px;font-weight:400;letter-spacing:-1px}
  .app-header__refresh{position:absolute;left:469px;top:0;width:85px;height:71px;border-left:1px solid var(--brand-blue-dark);display:flex;align-items:center;justify-content:center}

  .canteen{position:absolute;left:0;width:553px;height:166px;border-bottom:2px solid var(--row-line);background:var(--row-bg)}
  .canteen__name{position:absolute;left:17px;top:14px;font-size:27px;font-weight:700;line-height:31px;color:var(--heading-grey)}
  .canteen__distance{position:absolute;left:17px;top:94px;font-size:21px;color:var(--meta-grey);display:flex;align-items:center;gap:6px;font-weight:700}
  .canteen__address{position:absolute;left:17px;top:126px;font-size:21px;color:var(--link-blue)}
  .canteen__fav{position:absolute;left:465px;top:49px;width:70px;height:70px;border-radius:5px;background:var(--button-grey);display:flex;align-items:center;justify-content:center}

  .tab-bar{position:absolute;left:0;top:749px;width:553px;height:78px;background:var(--tab-bg);display:flex}
  .tab{flex:1;border-right:2px solid var(--tab-line);display:flex;flex-direction:column;align-items:center;justify-content:flex-end;padding-bottom:2px;color:#e0e0e0;font-size:19px}
  .tab:last-child{border-right:0}
  .tab svg{margin-bottom:4px}
  .tab--active{background:#1f1f1f}

  .date-band{position:absolute;left:0;top:104px;width:100%;height:56px;background:var(--date-band);border-bottom:2px solid var(--row-line);padding-left:18px;line-height:56px;font-size:25px;font-weight:700;color:var(--meta-grey)}
  .meal{position:absolute;left:0;width:554px;height:182px;background:#ebebeb;border-bottom:2px solid var(--row-line)}
  .meal__category{position:absolute;left:10px;top:10px;font-size:23px;color:var(--link-blue)}
  .meal__name{position:absolute;left:10px;top:46px;width:380px;font-size:29px;line-height:35px;color:var(--meal-grey)}
  .meal__prices{position:absolute;left:10px;top:138px;font-family:"Roboto Condensed","Arial Narrow",sans-serif;font-size:27px;color:var(--link-blue);display:flex;align-items:center}
  .meal__prices span+span::before{content:"";display:inline-block;width:1px;height:20px;background:#b5b5b5;margin:0 8px;vertical-align:-2px}
  .meal__divider{position:absolute;left:354px;top:138px;width:1px;height:30px;background:#bdbdbd}
  .meal__rating{position:absolute;left:412px;top:140px;display:flex;gap:1px}
  .meal__photo{position:absolute;left:423px;top:10px;width:120px;height:120px;border-radius:8px;border:2px solid #fff;box-shadow:0 0 0 1px #c4c4c4}
</style>
</head>
<body>
<div class="stage">

  <!-- Canteen list -->
  <section class="screen screen--canteens">
    <div class="status-bar" style="height:34px">
      <div class="status-bar__carrier">
        <svg width="30" height="16" viewBox="0 0 30 16"><rect x="0" y="12" width="4" height="4" fill="#fff"/><rect x="6" y="9" width="4" height="7" fill="#fff"/><rect x="12" y="6" width="4" height="10" fill="#fff"/><rect x="18" y="3" width="4" height="13" fill="#fff"/><rect x="24" y="0" width="4" height="16" fill="#fff"/></svg>
        <span>VERVE</span><span style="margin-left:6px">3G</span>
      </div>
      <svg class="status-bar__lock" width="20" height="22" viewBox="0 0 20 22"><path d="M5 10V6a5 5 0 0 1 10 0v4" stroke="#fff" stroke-width="2.5" fill="none"/><rect x="2" y="10" width="16" height="12" fill="#fff"/></svg>
      <svg class="status-bar__battery" width="38" height="18" viewBox="0 0 38 18"><rect x="1" y="1" width="32" height="16" rx="2" stroke="#fff" stroke-width="2" fill="none"/><rect x="4" y="4" width="26" height="10" fill="#fff"/><rect x="34" y="6" width="3" height="6" fill="#fff"/></svg>
    </div>
    <header class="app-header" style="top:34px">
      <h1 class="app-header__title">label</h1>
      <div class="app-header__refresh">
        <svg width="48" height="48" viewBox="0 0 48 48" fill="none" stroke="#fff" stroke-width="3"><circle cx="24" cy="24" r="22"/><path d="M14 22a10 10 0 0 1 18-5"/><path d="M34 26a10 10 0 0 1-18 5"/><path d="M33 11v7h-7" stroke-linejoin="round"/><path d="M15 37v-7h7" stroke-linejoin="round"/></svg>
      </div>
    </header>

    <article class="canteen" style="top:110px">
      <h2 class="canteen__name">Baden-Wurttemberg<br>Lorem Ipsum</h2>
      <p class="canteen__distance"><svg width="14" height="20" viewBox="0 0 14 20"><path d="M7 0a7 7 0 0 1 7 7c0 5-7 13-7 13S0 12 0 7a7 7 0 0 1 7-7z" fill="#6f6f6f"/><circle cx="7" cy="7" r="2.6" fill="#e7e7e7"/></svg>Deistance : 185 km</p>
      <p class="canteen__address">Kastanienallee 45, 70174 Stuttgart</p>
      <div class="canteen__fav"><svg width="38" height="32" viewBox="0 0 38 32"><path d="M19 32 3 16A9 9 0 0 1 19 5a9 9 0 0 1 16 11z" fill="#2566c4"/></svg></div>
    </article>
    <article class="canteen" style="top:278px">
      <h2 class="canteen__name">Baden-Wurttemberg<br>Lorem Ipsum</h2>
      <p class="canteen__distance"><svg width="14" height="20" viewBox="0 0 14 20"><path d="M7 0a7 7 0 0 1 7 7c0 5-7 13-7 13S0 12 0 7a7 7 0 0 1 7-7z" fill="#6f6f6f"/><circle cx="7" cy="7" r="2.6" fill="#e7e7e7"/></svg>Deistance : 185 km</p>
      <p class="canteen__address">Kastanienallee 45, 70174 Stuttgart</p>
      <div class="canteen__fav"><svg width="38" height="32" viewBox="0 0 38 32"><path d="M19 32 3 16A9 9 0 0 1 19 5a9 9 0 0 1 16 11z" fill="#ececec"/></svg></div>
    </article>
    <article class="canteen" style="top:446px">
      <h2 class="canteen__name">Baden-Wurttemberg</h2>
      <p class="canteen__distance"><svg width="14" height="20" viewBox="0 0 14 20"><path d="M7 0a7 7 0 0 1 7 7c0 5-7 13-7 13S0 12 0 7a7 7 0 0 1 7-7z" fill="#6f6f6f"/><circle cx="7" cy="7" r="2.6" fill="#e7e7e7"/></svg>Deistance : 185 km</p>
      <p class="canteen__address">Kastanienallee 45, 70174 Stuttgart</p>
      <div class="canteen__fav"><svg width="38" height="32" viewBox="0 0 38 32"><path d="M19 32 3 16A9 9 0 0 1 19 5a9 9 0 0 1 16 11z" fill="#2566c4"/></svg></div>
    </article>
    <article class="canteen" style="top:614px">
      <h2 class="canteen__name">Baden-Wurttemberg</h2>
      <p class="canteen__distance"><svg width="14" height="20" viewBox="0 0 14 20"><path d="M7 0a7 7 0 0 1 7 7c0 5-7 13-7 13S0 12 0 7a7 7 0 0 1 7-7z" fill="#6f6f6f"/><circle cx="7" cy="7" r="2.6" fill="#e7e7e7"/></svg>Deistance : 185 km</p>
      <p class="canteen__address">Kastanienallee 45, 70174 Stuttgart</p>
      <div class="canteen__fav"><svg width="38" height="32" viewBox="0 0 38 32"><path d="M19 32 3 16A9 9 0 0 1 19 5a9 9 0 0 1 16 11z" fill="#2566c4"/></svg></div>
    </article>

    <nav class="tab-bar">
      <div class="tab tab--active">
        <svg width="48" height="40" viewBox="0 0 48 40" fill="none" stroke="#2f78d8" stroke-width="3.5" stroke-linecap="round"><path d="M8 4l14 14M4 8l14 14M6 6l22 22M26 26l10 10"/><path d="M40 4c-6 2-12 10-12 14l-18 18"/><path d="M40 4c2 6-4 14-10 16"/></svg>
        <span>Canteens</span>
      </div>
      <div class="tab">
        <svg width="28" height="40" viewBox="0 0 28 40"><path d="M14 0a14 14 0 0 1 14 14c0 10-14 26-14 26S0 24 0 14A14 14 0 0 1 14 0z" fill="#c9c9c9"/><circle cx="14" cy="14" r="5" fill="#262626"/></svg>
        <span>Map</span>
      </div>
      <div class="tab">
        <svg width="38" height="34" viewBox="0 0 38 32"><path d="M19 32 3 16A9 9 0 0 1 19 5a9 9 0 0 1 16 11z" fill="#c9c9c9"/></svg>
        <span>Favorites</span>
      </div>
    </nav>
  </section>

  <!-- Meal list -->
  <section class="screen screen--menu">
    <div class="status-bar" style="height:30px">
      <div class="status-bar__carrier">
        <svg width="30" height="16" viewBox="0 0 30 16"><rect x="0" y="12" width="4" height="4" fill="#fff"/><rect x="6" y="9" width="4" height="7" fill="#fff"/><rect x="12" y="6" width="4" height="10" fill="#fff"/><rect x="18" y="3" width="4" height="13" fill="#fff"/><rect x="24" y="0" width="4" height="16" fill="#fff"/></svg>
        <span>VERVE</span><span style="margin-left:6px">3G</span>
      </div>
      <svg class="status-bar__lock" width="20" height="22" viewBox="0 0 20 22"><path d="M5 10V6a5 5 0 0 1 10 0v4" stroke="#fff" stroke-width="2.5" fill="none"/><rect x="2" y="10" width="16" height="12" fill="#fff"/></svg>
      <svg class="status-bar__battery" width="38" height="18" viewBox="0 0 38 18"><rect x="1" y="1" width="32" height="16" rx="2" stroke="#fff" stroke-width="2" fill="none"/><rect x="4" y="4" width="26" height="10" fill="#fff"/><rect x="34" y="6" width="3" height="6" fill="#fff"/></svg>
    </div>
    <header class="app-header" style="top:30px">
      <h1 class="app-header__title">label</h1>
      <div class="app-header__refresh">
        <svg width="48" height="48" viewBox="0 0 48 48" fill="none" stroke="#fff" stroke-width="3"><circle cx="24" cy="24" r="22"/><path d="M14 22a10 10 0 0 1 18-5"/><path d="M34 26a10 10 0 0 1-18 5"/><path d="M33 11v7h-7" stroke-linejoin="round"/><path d="M15 37v-7h7" stroke-linejoin="round"/></svg>
      </div>
    </header>

    <div class="date-band">May 15, 2013</div>

    <article class="meal" style="top:162px">
      <p class="meal__category">Beilagen</p>
      <h2 class="meal__name">Kartoffelpuffer mit Apfel-mus</h2>
      <p class="meal__prices"><span>€0.60</span><span>€1.00</span><span>€1.00</span><span>€1.00</span></p>
      <div class="meal__divider"></div>
      <svg class="meal__rating" width="128" height="24" viewBox="0 0 128 24"><g id="s"><polygon points="12,1 15,9 23,9 17,14 19,23 12,18 5,23 7,14 1,9 9,9" fill="var(--star-on)"/></g><use href="#s" x="25"/><use href="#s" x="50"/><polygon transform="translate(75)" points="12,1 15,9 23,9 17,14 19,23 12,18 5,23 7,14 1,9 9,9" fill="var(--star-off)"/><polygon transform="translate(100)" points="12,1 15,9 23,9 17,14 19,23 12,18 5,23 7,14 1,9 9,9" fill="var(--star-off)"/></svg>
    </article>

    <article class="meal" style="top:344px">
      <p class="meal__category">Beilagen</p>
      <h2 class="meal__name">Butterreis</h2>
      <div class="meal__photo" role="img" aria-label="Photo of the meal: pasta with vegetables" style="background:linear-gradient(160deg,#5d7a3a 0%,#c98a3c 45%,#e0b35a 70%,#b0462c 100%)"></div>
      <p class="meal__prices"><span>€0.60</span><span>€1.00</span><span>€1.00</span></p>
      <div class="meal__divider"></div>
      <svg class="meal__rating" width="128" height="24" viewBox="0 0 128 24"><g fill="var(--star-off)"><polygon points="12,1 15,9 23,9 17,14 19,23 12,18 5,23 7,14 1,9 9,9"/><polygon transform="translate(25)" points="12,1 15,9 23,9 17,14 19,23 12,18 5,23 7,14 1,9 9,9"/><polygon transform="translate(50)" points="12,1 15,9 23,9 17,14 19,23 12,18 5,23 7,14 1,9 9,9"/><polygon transform="translate(75)" points="12,1 15,9 23,9 17,14 19,23 12,18 5,23 7,14 1,9 9,9"/><polygon transform="translate(100)" points="12,1 15,9 23,9 17,14 19,23 12,18 5,23 7,14 1,9 9,9"/></g></svg>
    </article>

    <article class="meal" style="top:526px">
      <h2 class="meal__name" style="top:46px">Kartoffelpuffer mit Apfel-mus</h2>
      <div class="meal__photo" role="img" aria-label="Photo of the meal: fried dumplings with greens" style="left:415px;background:linear-gradient(150deg,#9fb07a 0%,#e8d6b0 40%,#e08a3a 70%,#c0522a 100%)"></div>
      <p class="meal__prices"><span>€0.60</span><span>€1.00</span></p>
      <div class="meal__divider"></div>
      <svg class="meal__rating" width="128" height="24" viewBox="0 0 128 24"><g fill="var(--star-on)"><polygon points="12,1 15,9 23,9 17,14 19,23 12,18 5,23 7,14 1,9 9,9"/><polygon transform="translate(25)" points="12,1 15,9 23,9 17,14 19,23 12,18 5,23 7,14 1,9 9,9"/><polygon transform="translate(50)" points="12,1 15,9 23,9 17,14 19,23 12,18 5,23 7,14 1,9 9,9"/></g><g fill="var(--star-off)"><polygon transform="translate(75)" points="12,1 15,9 23,9 17,14 19,23 12,18 5,23 7,14 1,9 9,9"/><polygon transform="translate(100)" points="12,1 15,9 23,9 17,14 19,23 12,18 5,23 7,14 1,9 9,9"/></g></svg>
    </article>

    <article class="meal" style="top:708px">
      <p class="meal__category">Beilagen</p>
      <h2 class="meal__name">Kartoffelpuffer mit Apfel-mus</h2>
    </article>
  </section>

</div>
</body>
</html>
```